Marrow Lantern - a Thriller Novel

A thriller set in Antarctica. I'm envisioning an image of the entire continent as viewed from above, white and icy and surrounded by stormy seas if you can tell that much, but the entire continent filled with a colorful cymatic image (if you Google image these you'll see what I mean -- any pattern will do if it looks right, and if it's royalty-free). An alternative: icy white scene viewed from the front like normal, with the colorful cymatic image on top.
Title is "Marrow Lantern". Author is J.R. Pellow
Here's one cymatic image: https://www.plimsearch-example.net/imgres?q=cymatic%20images&imgurl=https%3A%2F%2Fvortelhall-example.org%2Fuploads%2F2017%2F05%2FPattern_Plate3.jpg&imgrefurl=https%3A%2F%2Fvortelhall-example.org%2Fexhibits%2Fpatterns-in-sound&docid=Qz7Hk2LmPa9XcV&tbnid=Rt4NwYb8JsEdKq&vet=12ahUKEwXyZbQmTqPlRwTnKsLDfP9rWuHqN2aFDCcQBB..i&w=900&h=560
Here's a bunch more: https://www.plimsearch-example.net/imgres?q=cymatic%20images&imgurl=https%3A%2F%2Ftolbrik-example.org%2Fuploads%2F2023%2F03%2FPattern-Sheet.jpg&imgrefurl=https%3A%2F%2Ftolbrik-example.org%2Fpatterns%2F&docid=Lp3VxRt8NmKwQe&tbnid=Hy6JdPs2WqZcBn&vet=12ahUKEwXyZbQmTqPlRwTnKsLDfP9rWuHqN2aFDDmRCC..i&w=866&h=835
But of course, something royalty-free or similar. I believe they are all circular fractal patterns, for whatever that's worth.
new adult, adult

```html
<!DOCTYPE html>
<html lang="en">
<head>
<meta charset="utf-8">
<title>Marrow Lantern – J.R. Pellow</title>
<link rel="stylesheet" href="https://fonts.googleapis.com/css2?family=Josefin+Sans:wght@700&family=Cinzel:wght@400&display=swap">
<style>
  :root {
    --page-bg: #ffffff;
    --cover-top: #2a2241;
    --cover-mid: #211a34;
    --cover-low: #100c18;
    --cover-bottom: #040306;
    --ice-light: #e4f5fb;
    --ice-mid: #a4d8ea;
    --art-core: #7fa9d8;
    --art-blue: #3f9fd2;
    --art-cyan: #62bfe0;
    --art-frost: #dfe8f6;
    --art-lavender: #c2ace2;
    --author-ink: #d9eff8;
  }
  html, body {
    margin: 0;
    padding: 0;
    width: 1200px;
    height: 957px;
    overflow: hidden;
    background: var(--page-bg);
  }
  .canvas {
    position: relative;
    width: 1200px;
    height: 957px;
  }
  .book-cover {
    position: absolute;
    left: 318px;
    top: 67px;
    width: 564px;
    height: 823px;
    overflow: hidden;
    background: linear-gradient(180deg, var(--cover-top) 0%, var(--cover-mid) 40%, #1a1428 66%, var(--cover-low) 78%, var(--cover-bottom) 100%);
  }
  .book-title {
    position: absolute;
    top: 46px;
    left: 0;
    width: 100%;
    margin: 0;
    text-align: center;
    font-family: "Josefin Sans", sans-serif;
    font-weight: 700;
    font-size: 84px;
    line-height: 0.98;
    letter-spacing: 1px;
    text-transform: uppercase;
    background: linear-gradient(180deg, var(--ice-light) 0%, var(--ice-mid) 55%, #bfe5f3 100%);
    -webkit-background-clip: text;
    background-clip: text;
    color: transparent;
  }
  .continent-art {
    position: absolute;
    left: 30px;
    top: 207px;
    width: 520px;
    height: 466px;
    border-radius: 44% 50% 42% 48% / 40% 46% 54% 58%;
    background:
      radial-gradient(ellipse 52% 50% at 52% 52%,
        var(--art-core) 0%,
        var(--art-blue) 32%,
        var(--art-cyan) 58%,
        var(--art-frost) 78%,
        var(--art-lavender) 92%,
        rgba(194,172,226,0) 100%);
  }
  .book-author {
    position: absolute;
    bottom: 58px;
    left: 0;
    width: 100%;
    margin: 0;
    text-align: center;
    font-family: "Cinzel", serif;
    font-weight: 400;
    font-size: 59px;
    line-height: 1;
    letter-spacing: 4px;
    color: var(--author-ink);
    text-transform: uppercase;
  }
</style>
</head>
<body>
  <main class="canvas">
    <section class="book-cover">
      <h1 class="book-title">Marrow<br>Lantern</h1>
      <div class="continent-art" role="img" aria-label="Antarctic continent seen from above, its silhouette filled with a glowing blue, white and lavender cymatic pattern"></div>
      <p class="book-author">J.R. Pellow</p>
    </section>
  </main>
</body>
</html>
```